PRICE LIST

I wont a design similar to my business card but not black i wont it very easy to read and simple here is my price list so far

Industry/Entity Type

Business

Font styles to use
Script

```html
<!DOCTYPE html>
<html lang="en">
<head>
<meta charset="utf-8">
<title>Simple Glow GC – Price List</title>
<link rel="stylesheet" href="https://fonts.googleapis.com/css2?family=Gelasio:wght@400;700&family=Kaushan+Script&family=Arimo:wght@400&display=swap">
<style>
  :root {
    --paper: #ffffff;
    --frame: #9a9a9a;
    --maroon: #8e1c22;
    --gold: #c5a063;
    --gold-soft: #e3cfa6;
    --ink: #1c1c1c;
    --grey-mark: #bdbdbd;
    --serif: "Gelasio", Georgia, serif;
    --script: "Kaushan Script", cursive;
    --sans: "Arimo", Arial, sans-serif;
  }
  * { box-sizing: border-box; margin: 0; padding: 0; }
  html, body { width: 844px; height: 1200px; overflow: hidden; background: var(--paper); }
  .price-list {
    position: relative;
    width: 844px; height: 1200px;
    background: var(--paper);
  }
  .page-frame {
    position: absolute; inset: 4px;
    border: 1.5px solid var(--frame);
  }
  .abs { position: absolute; }

  /* Header */
  .brand-name {
    top: 30px; left: 0; width: 844px;
    text-align: center;
    font-family: var(--serif); font-weight: 400;
    font-size: 64px; color: var(--gold);
    letter-spacing: 1px;
  }
  .flourish {
    left: 250px; width: 344px; height: 38px; top: 115px;
    background: linear-gradient(90deg, transparent, var(--gold-soft) 20%, var(--gold) 50%, var(--gold-soft) 80%, transparent);
    border-radius: 20px;
    opacity: .75;
  }
  .flourish-lower {
    left: 320px; width: 204px; height: 70px; top: 172px;
    background: radial-gradient(ellipse at center, var(--gold) 0%, var(--gold-soft) 55%, transparent 75%);
    border-radius: 50%;
    opacity: .8;
  }
  .tagline {
    top: 137px; left: 0; width: 844px;
    text-align: center;
    font-family: var(--script); font-size: 25px;
    color: var(--gold);
    background: transparent;
  }

  /* Section headings */
  .section-title {
    font-family: var(--serif); font-weight: 700;
    font-size: 26px; color: var(--maroon);
    top: 292px;
  }
  .title-nails { left: 41px; }
  .title-wax { left: 526px; }

  /* Nail services */
  .service {
    left: 41px; width: 370px;
    font-family: var(--serif); font-size: 18.5px; line-height: 25px;
    color: var(--ink);
  }
  .service-name { color: var(--maroon); display: block; }
  .service-price {
    position: absolute; right: 0; top: 0;
    color: var(--maroon);
  }

  /* Waxing list */
  .wax-item {
    left: 519px; width: 210px;
    font-family: var(--serif); font-size: 18.5px;
    color: var(--ink);
  }
  .wax-item .service-price { color: var(--ink); }

  /* Partner marks */
  .partner {
    left: 519px; width: 300px;
    display: flex; align-items: center; justify-content: center; gap: 12px;
    font-family: var(--serif); font-weight: 400; color: var(--ink);
  }
  .partner-square { width: 30px; height: 30px; background: var(--ink); }
  .partner-circle { width: 40px; height: 40px; border-radius: 50%; background: var(--ink); }
  .partner-nails { top: 600px; font-size: 44px; }
  .partner-tan { top: 730px; font-size: 42px; }
  .tan-offer {
    left: 490px; width: 350px; top: 828px;
    text-align: center;
    font-family: var(--sans); font-size: 15.5px; line-height: 22px;
    color: var(--ink);
  }

  /* Social */
  .social {
    top: 902px; width: 200px;
    display: flex; flex-direction: column; align-items: center; gap: 10px;
    font-family: var(--sans); font-size: 13px; color: var(--ink);
  }
  .social-square {
    width: 66px; height: 66px; border-radius: 8px;
    background: var(--grey-mark);
  }
  .social-left { left: 255px; }
  .social-right { left: 405px; }

  /* Contact */
  .contact {
    top: 1030px; left: 0; width: 844px;
    text-align: center;
    font-family: var(--sans); font-size: 17px; line-height: 27.5px;
    color: var(--maroon);
    font-style: normal;
  }
</style>
</head>
<body>
<main class="price-list">
  <div class="page-frame"></div>

  <header>
    <h1 class="abs brand-name">Simple Glow GC</h1>
    <div class="abs flourish" role="img" aria-label="Gold ornamental scroll flourish beneath the business name"></div>
    <p class="abs tagline">Simple but Splendid services</p>
    <div class="abs flourish-lower" role="img" aria-label="Gold ornamental scroll flourish beneath the tagline"></div>
  </header>

  <h2 class="abs section-title title-nails">Manicures &amp; Pedicures</h2>
  <h2 class="abs section-title title-wax">Waxing &amp; Tinting</h2>

  <section>
    <div class="abs service" style="top:347px"><span class="service-name">Gloss Gel Manicure</span><span class="service-price">$ 30</span>Cut, shape, cuticles &amp; Gloss Gel</div>
    <div class="abs service" style="top:412px"><span class="service-name">Deluxe Manicure</span><span class="service-price">$ 40</span>Soak, exfoliate, cut, shape, cuticles<br>&amp; polish or add gloss gel for $10</div>
    <div class="abs service" style="top:502px"><span class="service-name">Paraffin Manicure</span><span class="service-price">$ 45</span>Soak, exfoliate, paraffin treatment,<br>Cut, shape, cuticles<br>&amp; polish or add gloss gel for $ 5</div>
    <div class="abs service" style="top:615px"><span class="service-name">Gloss Gel Pedicure</span><span class="service-price">$ 30</span>Cut, shape, cuticles &amp; Gloss Gel</div>
    <div class="abs service" style="top:679px"><span class="service-name">Deluxe Pedicure</span><span class="service-price">$ 40</span>Soak, exfoliate, cut, shape, cuticles<br>&amp; polish or add gloss gel for $10</div>
    <div class="abs service" style="top:766px"><span class="service-name">Paraffin Pedicure</span><span class="service-price">$ 45</span>Soak, exfoliate, paraffin treatment,<br>Cut, shape, cuticles<br>&amp; polish or add gloss gel for $ 5</div>
  </section>

  <section>
    <div class="abs wax-item" style="top:347px">Eyebrow Wax<span class="service-price">$ 10</span></div>
    <div class="abs wax-item" style="top:385px">Eyebrow tint<span class="service-price">$ 10</span></div>
    <div class="abs wax-item" style="top:423px">Eyelash Tint<span class="service-price">$ 10</span></div>
    <div class="abs wax-item" style="top:461px">Lip Wax<span class="service-price">$ 10</span></div>
    <div class="abs wax-item" style="top:499px">Chin Wax<span class="service-price">$ 10</span></div>
    <div class="abs wax-item" style="top:537px">Underarm<span class="service-price">$ 15</span></div>

    <div class="abs partner partner-nails"><span>Nailora</span><span class="partner-square"></span></div>
    <div class="abs partner partner-tan"><span class="partner-circle"></span><span>SunVeil</span></div>
    <p class="abs tan-offer">The very popular "2 hour SUNVEIL"<br>in all ranges is now available for $25.00!</p>
  </section>

  <section>
    <div class="abs social social-left"><span class="social-square"></span>Simple Glow Gold Coast</div>
    <div class="abs social social-right"><span class="social-square"></span>simpleglowgoldcoast</div>
  </section>

  <address class="abs contact">
    Maren<br>
    Coral Heights,<br>
    Sunshore, Queensland 4299<br>
    Ph.: +61 400 555 019<br>
    Flexible Hours 7 Days a week<br>
    hello@simpleglowgc.com
  </address>
</main>
</body>
</html>
```